VMR business card

Need a business card for a company that provides instructional design and elearning development services. The website is here: http://vantmoro.studio/

I'm attaching a current logo, as well as the old business card design. While I like to keep it clean, the old design is too simplistic for my liking. The only idea I want to reuse from the old design is placing industry jargon on the back of the card, just need a better way to present it. But if you have other ideas for the back--feel free to experiment.

Please use the colors complementary to the color we have on the website. Thank you!

```html
<!DOCTYPE html>
<html lang="en">
<head>
<meta charset="utf-8">
<title>VMR business card</title>
<link rel="stylesheet" href="https://fonts.googleapis.com/css2?family=Arimo:wght@400;700&family=Montserrat:wght@500;700&display=swap">
<style>
  :root{
    --bg:#e9e9e7;
    --sand:#ddd08f;
    --teal:#19a89c;
    --ink:#3c3c3c;
    --charcoal:#3a3b3b;
    --white:#ffffff;
  }
  *{box-sizing:border-box;margin:0;padding:0}
  html,body{width:1200px;height:900px;overflow:hidden;background:var(--bg)}
  .stage{position:relative;width:1200px;height:900px}
  .card{position:absolute;left:250px;width:700px;height:400px;border-radius:26px;overflow:hidden;box-shadow:0 6px 18px rgba(0,0,0,.18)}
  .card-back{top:30px;background:var(--sand)}
  .card-front{top:470px;background:var(--white)}

  .jargon{position:absolute;left:110px;top:62px;font-family:"Arimo",Arial,sans-serif;font-size:31px;line-height:41px;
    color:var(--ink);letter-spacing:1.5px;text-transform:uppercase;white-space:nowrap}
  .jargon .cta{color:var(--teal);font-weight:700;font-size:35px;letter-spacing:1px}

  .front-shapes{position:absolute;inset:0}
  .brand{position:absolute;left:40px;top:74px;display:flex;align-items:center;gap:16px;
    font-family:"Montserrat",Arial,sans-serif;font-weight:700;font-size:64px;color:var(--teal);letter-spacing:4px}
  .brand-dot{width:40px;height:40px;border-radius:50%;background:var(--teal)}
  .holder-name{position:absolute;right:36px;top:192px;font-family:"Montserrat",Arial,sans-serif;font-weight:700;
    font-size:24px;color:var(--teal);letter-spacing:.5px;white-space:nowrap}
  .contacts{position:absolute;left:28px;top:330px;list-style:none;font-family:"Montserrat",Arial,sans-serif;
    font-weight:700;font-size:17px;color:var(--white);line-height:22px;white-space:nowrap}
  .contacts li{display:flex;align-items:center;gap:10px}
  .contacts svg{width:14px;height:14px;flex:none}
</style>
</head>
<body>
<main class="stage">

  <section class="card card-back" aria-label="Card back">
    <p class="jargon">
      Mobile learning SCORM<br>
      Instructional design LMS<br>
      MOOCs eLearning HTML5<br>
      <span class="cta">How can we help?</span><br>
      Adult learning theory<br>
      Gamification classroom<br>
      xAPI blended learning
    </p>
  </section>

  <section class="card card-front" aria-label="Card front">
    <svg class="front-shapes" viewBox="0 0 700 400" preserveAspectRatio="none" aria-hidden="true">
      <polygon points="0,318 340,318 440,236 520,236 475,400 0,400" fill="var(--teal)"/>
      <polygon points="500,236 700,236 700,284 470,284" fill="var(--charcoal)"/>
    </svg>

    <div class="brand"><span class="brand-dot"></span>VMR</div>
    <div class="holder-name">DARIA KOVALENKO</div>

    <ul class="contacts">
      <li>
        <svg viewBox="0 0 24 24"><path fill="#fff" d="M6.6 10.8a15.1 15.1 0 0 0 6.6 6.6l2.2-2.2a1 1 0 0 1 1-.25 11.4 11.4 0 0 0 3.6.57 1 1 0 0 1 1 1V20a1 1 0 0 1-1 1A17 17 0 0 1 3 4a1 1 0 0 1 1-1h3.5a1 1 0 0 1 1 1c0 1.25.2 2.45.57 3.570a1 1 0 0 1-.25 1z"/></svg>
        555-014-2287
      </li>
      <li>
        <svg viewBox="0 0 24 24" fill="none" stroke="#fff" stroke-width="2"><circle cx="12" cy="12" r="9"/><path d="M3 12h18M12 3c3 3 3 15 0 18M12 3c-3 3-3 15 0 18"/></svg>
        www.vantmoro.studio
      </li>
      <li>
        <svg viewBox="0 0 24 24" fill="none" stroke="#fff" stroke-width="2"><rect x="3" y="5" width="18" height="14" rx="1"/><path d="M3 6l9 7 9-7"/></svg>
        dkovalenko@vantmoro.studio
      </li>
    </ul>
  </section>

</main>
</body>
</html>
```